Business Cards & Stationary for Dental Laboratory
Lumora Porcelain, Inc.
Business Cards & Stationary for Dental Laboratory - Medical
Creative Brief
Professional
Dov Pemberly, CDT & Lisette Pemberly
Technical ------ Marketing/Office
871 Talvenor Trade Ct Apopka, Fl 32719
lumoraporcelain@mailvex.net
lumoraporcelain.net
FL License #DL6042
I want to use our new logo. I would like to see some ideas with and without the format of the way it is set up. I want the same colors as in the logo. I would like to see some with the same font as logo and some other ideas. There are 2 names Dov is technical Lisette is marketing/office

```html
<!DOCTYPE html>
<html lang="en">
<head>
<meta charset="utf-8">
<title>Lumora Porcelain, Inc. — Stationery Concepts</title>
<link rel="stylesheet" href="https://fonts.googleapis.com/css2?family=Cinzel:wght@400&family=Michroma&family=Open+Sans:wght@400;600;700&family=Tinos&display=swap">
<style>
:root{
  --board:#8d8e90;
  --board-dark:#7c7d80;
  --ink:#1f1d1e;
  --panel:#231f20;
  --blue:#1e8fd6;
  --navy:#1e2fa8;
  --slate:#4a4a4c;
  --paper:#ffffff;
  --paper-shade:#ececec;
  --grey-text:#5c5c5c;
  --label:#f2f2f2;
}
*{margin:0;padding:0;box-sizing:border-box}
html,body{width:1200px;height:319px;overflow:hidden}
body{background:linear-gradient(180deg,var(--board) 0%,var(--board-dark) 100%);font-family:"Open Sans",sans-serif;position:relative;color:var(--ink)}
.piece{position:absolute}
.sheet{background:linear-gradient(135deg,var(--paper) 0%,var(--paper-shade) 100%);box-shadow:0 1px 3px rgba(0,0,0,.35);overflow:hidden}
.sheet.rounded{border-radius:4px}

/* edge accent: straight dark bar with a thin blue rule */
.edge{position:absolute;top:0;bottom:0;right:0;background:var(--panel)}
.edge::before{content:"";position:absolute;top:0;bottom:0;left:-2px;width:1px;background:var(--blue)}
.edge.left{right:auto;left:0}
.edge.left::before{left:auto;right:-2px}

.label{position:absolute;font-family:"Tinos",serif;font-size:5px;color:var(--label);text-align:center;transform:translateX(-50%);white-space:nowrap}
.brand{display:flex;align-items:center;gap:3px}
.brand-dot{border-radius:50%;background:var(--ink);flex:none}
.brand-name{font-family:"Michroma",sans-serif;color:var(--ink);line-height:1.15;text-transform:uppercase;white-space:nowrap}
.brand-name span{display:block}
.tagline{font-family:"Open Sans",sans-serif;color:var(--grey-text);white-space:nowrap}
.faint-mark{position:absolute;border-radius:40%;background:radial-gradient(ellipse at center,rgba(30,143,214,.10) 0%,rgba(180,180,180,.10) 55%,rgba(255,255,255,0) 75%)}
.tiny{font-size:2.6px;line-height:1.45;color:var(--ink);white-space:nowrap}
.tiny b{font-weight:700;font-size:3.4px}
.icon{display:inline-block;width:2.4px;height:2.4px;border-radius:50%;background:var(--ink);margin-right:1px;vertical-align:middle}

/* board heading */
.board-title{left:17px;top:64px}
.board-title .brand-dot{width:12px;height:12px}
.board-title .brand-name{font-size:8.6px}
.board-title .tagline{font-size:4.6px;margin:3px 0 0 15px}
.board-heading{left:24px;top:113px;font-family:"Cinzel",serif;font-size:9.5px;color:#f4f4f4;letter-spacing:.06em}

/* business cards */
.card-front{left:18px;top:148px;width:120px;height:67px}
.card-front .edge{width:6px}
.card-front .brand{position:absolute;left:6px;top:25px}
.card-front .brand-dot{width:5px;height:5px}
.card-front .brand-name{font-size:3.6px}
.card-front .tagline{position:absolute;left:14px;top:36px;font-size:2.3px}
.card-front .lic{position:absolute;left:14px;top:41px;font-weight:700}
.card-front .people{position:absolute;left:70px;top:5px}
.card-front .contact{position:absolute;left:70px;top:39px}

.card-back{left:17px;top:234px;width:122px;height:68px;background:var(--paper)}
.card-back .faint-mark{left:38px;top:6px;width:50px;height:56px}

/* letterhead */
.letterhead{left:154px;top:39px;width:203px;height:263px}
.letterhead .edge{width:8px}
.letterhead .brand{position:absolute;left:64px;top:8px}
.letterhead .brand-dot{width:8px;height:8px}
.letterhead .brand-name{font-size:5.6px}
.letterhead .tagline{position:absolute;left:75px;top:24px;font-size:2.8px}
.letterhead .faint-mark{left:55px;top:55px;width:90px;height:120px}
.letterhead .body{position:absolute;left:14px;top:57px;width:170px;font-size:3.3px;line-height:1.5;color:#444}
.letterhead .body p{margin-bottom:4px}
.letterhead .body .recipient{font-weight:700;color:var(--ink)}
.letterhead .signature{position:absolute;left:15px;top:205px;width:45px;height:14px;background:linear-gradient(90deg,rgba(30,30,30,.18),rgba(30,30,30,.05));border-radius:2px}
.letterhead .sign-name{position:absolute;left:31px;top:219px;font-size:3.3px;font-weight:700}
.letterhead .sign-role{position:absolute;left:31px;top:224px;font-size:2.8px;color:#555}
.letterhead .foot{position:absolute;right:13px;bottom:4px;text-align:right;font-size:2.4px;line-height:1.6;white-space:nowrap}

/* email signature */
.email-sig{left:405px;top:122px;width:138px;height:67px}
.email-sig .edge{width:6px}
.email-sig .brand{position:absolute;left:40px;top:7px}
.email-sig .brand-dot{width:5px;height:5px}
.email-sig .brand-name{font-size:4.2px}
.email-sig .tagline{position:absolute;left:48px;top:20px;font-size:2.4px}
.email-sig .people{position:absolute;right:68px;top:31px;text-align:right}
.email-sig .contact{position:absolute;left:74px;top:31px}

/* envelope front */
.env-front{left:369px;top:207px;width:220px;height:95px}
.env-front .edge{width:7px}
.env-front .brand{position:absolute;left:6px;top:7px}
.env-front .brand-dot{width:6px;height:6px}
.env-front .brand-name{font-size:4.8px}
.env-front .tagline{position:absolute;left:15px;top:21px;font-size:2.7px}
.env-front .address{position:absolute;left:6px;top:30px}
.env-front .faint-mark{left:140px;top:8px;width:50px;height:75px}

/* envelope backs */
.env-back{position:absolute;width:220px;height:97px;background:var(--paper);box-shadow:0 1px 3px rgba(0,0,0,.35)}
.env-back .flap{position:absolute;left:0;top:0;width:100%;height:33px;border-radius:0 0 6px 6px;display:flex;justify-content:center;align-items:center}
.env-back .seal{width:9px;height:9px;border-radius:50%}
.env-back .folds{position:absolute;inset:0;width:100%;height:100%}
.env-blue{left:626px;top:103px}
.env-blue .flap{background:var(--navy)}
.env-blue .seal{background:var(--paper)}
.env-slate{left:612px;top:155px}
.env-slate .flap{background:var(--slate)}
.env-slate .seal{background:var(--paper)}
.env-white{left:598px;top:207px;height:95px}
.env-white .flap{background:linear-gradient(180deg,#fafafa,#ededed);box-shadow:0 1px 2px rgba(0,0,0,.2)}
.env-white .seal{background:var(--ink)}

/* folder */
.folder{left:860px;top:45px;width:324px;height:260px}
.folder .outer{position:absolute;inset:0;width:100%;height:100%}
.folder .faint-mark{left:50px;top:45px;width:60px;height:95px;background:radial-gradient(ellipse at center,rgba(255,255,255,.06),rgba(255,255,255,0) 70%)}
.folder .back-info{position:absolute;left:22px;top:142px;font-size:2.6px;line-height:1.55;color:#ddd;white-space:nowrap}
.folder .back-info .icon{background:var(--blue)}
.folder .cover{position:absolute;left:162px;top:1px;width:137px;height:188px;background:linear-gradient(135deg,var(--paper),#e9e9e9);overflow:hidden}
.folder .cover .edge{width:7px}
.folder .cover .brand{position:absolute;left:12px;top:80px}
.folder .cover .brand-dot{width:9px;height:9px}
.folder .cover .brand-name{font-size:7.2px}
.folder .cover .tagline{position:absolute;left:24px;top:101px;font-size:4px}
.folder .pocket-card{position:absolute;left:210px;top:205px;width:60px;height:33px;background:var(--paper);border-radius:2px;transform:rotate(-12deg);box-shadow:0 1px 2px rgba(0,0,0,.4);overflow:hidden}
.folder .pocket-card .brand{position:absolute;left:30px;top:4px}
.folder .pocket-card .brand-dot{width:3px;height:3px}
.folder .pocket-card .brand-name{font-size:2px}
.folder .pocket-card .mini{position:absolute;right:4px;top:14px;font-size:1.8px;line-height:1.5;text-align:right;white-space:nowrap}
</style>
</head>
<body>

<div class="piece board-title">
  <div class="brand"><span class="brand-dot"></span><span class="brand-name"><span>Lumora</span><span>Porcelain, Inc.</span></span></div>
  <div class="tagline">Precision crafted for every smile</div>
</div>
<div class="piece board-heading">Stationary Concepts</div>

<div class="piece sheet rounded card-front">
  <div class="edge"></div>
  <div class="brand"><span class="brand-dot"></span><span class="brand-name"><span>Lumora</span><span>Porcelain, Inc.</span></span></div>
  <div class="tagline">Precision crafted for every smile</div>
  <div class="tiny lic">FL License #DL6042</div>
  <div class="tiny people">
    <b>Dov Pemberly, CDT</b><br>Technical<br>
    <b>Lisette Pemberly</b><br>Marketing/Office<br><br>
    871 Talvenor Trade Ct<br>Marrowvale, Fl 32719
  </div>
  <div class="tiny contact">
    <span class="icon"></span>888-555-0140<br>
    <span class="icon"></span>407-555-0146<br>
    <span class="icon"></span>407-555-0188<br>
    <span class="icon"></span>lumoraporcelain@mailvex.net<br>
    <span class="icon"></span>lumoraporcelain.net
  </div>
</div>
<div class="label" style="left:77px;top:221px">Front Card</div>

<div class="piece sheet rounded card-back">
  <div class="faint-mark" role="img" aria-label="Faint decorative background mark"></div>
</div>
<div class="label" style="left:78px;top:307px">Back Card</div>

<div class="piece sheet letterhead">
  <div class="edge"></div>
  <div class="brand"><span class="brand-dot"></span><span class="brand-name"><span>Lumora</span><span>Porcelain, Inc.</span></span></div>
  <div class="tagline">Precision crafted for every smile</div>
  <div class="faint-mark" role="img" aria-label="Faint decorative background mark"></div>
  <div class="body">
    <p>Date</p>
    <p class="recipient">Recipient Name</p>
    <p>Company Name<br>Street Address<br>City, State, Zip</p>
    <p style="margin-top:8px">Lorem ipsum dolor sit amet, consectetuer adipiscing elit, sed diam nonummy nibh euismod tincidunt ut laoreet dolore magna aliquam erat volutpat. Ut wisi enim ad minim veniam, quis nostrud exerci tation ullamcorper suscipit lobortis nisl ut aliquip ex ea commodo consequat. Duis autem vel eum iriure dolor in hendrerit in vulputate velit esse molestie consequat, vel illum dolore eu feugiat.</p>
    <p>Nulla facilisis at vero eros et accumsan et iusto odio dignissim qui blandit praesent luptatum zzril delenit augue duis dolore te feugait nulla facilisi. Nam liber tempor cum soluta nobis eleifend option congue nihil imperdiet doming id quod mazim placerat facer possim assum.</p>
    <p>Legere me lius quod ii legunt saepius. Claritas est etiam processus dynamicus, qui sequitur mutationem consuetudium lectorum. Mirum est notare quam littera gothica, quam nunc putamus parum claram, anteposuerit litterarum formas humanitatis.</p>
    <p>Legere me lius quod ii legunt saepius. Claritas est etiam processus dynamicus, qui sequitur mutationem consuetudium lectorum.</p>
    <p style="margin-top:8px">Sincerely,</p>
  </div>
  <div class="signature" role="img" aria-label="Handwritten signature"></div>
  <div class="sign-name">Dov Pemberly, CDT</div>
  <div class="sign-role">Technical</div>
  <div class="foot">
    FL License #DL6042 &nbsp;&nbsp; 871 Talvenor Trade Ct, Marrowvale, Fl 32719<br>
    <span class="icon"></span>888-555-0140 <span class="icon"></span>407-555-0146 <span class="icon"></span>407-555-0188 <span class="icon"></span>lumoraporcelain@mailvex.net <span class="icon"></span>LumoraPorcelain.net
  </div>
</div>
<div class="label" style="left:251px;top:307px">Letterhead option_02</div>

<div class="piece sheet email-sig">
  <div class="edge"></div>
  <div class="brand"><span class="brand-dot"></span><span class="brand-name"><span>Lumora</span><span>Porcelain, Inc.</span></span></div>
  <div class="tagline">Precision crafted for every smile</div>
  <div class="tiny people">
    <b>Dov Pemberly, CDT</b><br>Technical<br>
    <b>Lisette Pemberly</b><br>Marketing/Office<br>
    871 Talvenor Trade Ct<br>Marrowvale, Fl 32719
  </div>
  <div class="tiny contact">
    FL License #DL6042<br><br>
    <span class="icon"></span>888-555-0140<br>
    <span class="icon"></span>407-555-0146<br>
    <span class="icon"></span>407-555-0188<br>
    <span class="icon"></span>lumoraporcelain@mailvex.net<br>
    <span class="icon"></span>lumoraporcelain.net
  </div>
</div>
<div class="label" style="left:471px;top:193px">Email Signature_01</div>

<div class="piece sheet env-front">
  <div class="edge"></div>
  <div class="brand"><span class="brand-dot"></span><span class="brand-name"><span>Lumora</span><span>Porcelain, Inc.</span></span></div>
  <div class="tagline">Precision crafted for every smile</div>
  <div class="tiny address">FL License #DL6042<br>871 Talvenor Trade Ct, Marrowvale, Fl 32719</div>
  <div class="faint-mark" role="img" aria-label="Faint decorative background mark"></div>
</div>
<div class="label" style="left:473px;top:307px">Envelope Front</div>

<div class="env-back env-blue">
  <svg class="folds" viewBox="0 0 220 97" preserveAspectRatio="none" aria-hidden="true">
    <path d="M0 97 L90 40 M220 97 L130 40" stroke="#e6e6e6" stroke-width=".6" fill="none"/>
  </svg>
  <div class="flap"><span class="seal"></span></div>
</div>
<div class="env-back env-slate">
  <svg class="folds" viewBox="0 0 220 97" preserveAspectRatio="none" aria-hidden="true">
    <path d="M0 97 L90 40 M220 97 L130 40" stroke="#e6e6e6" stroke-width=".6" fill="none"/>
  </svg>
  <div class="flap"><span class="seal"></span></div>
</div>
<div class="env-back env-white">
  <svg class="folds" viewBox="0 0 220 95" preserveAspectRatio="none" aria-hidden="true">
    <path d="M0 95 L95 40 L125 40 L220 95" stroke="#e2e2e2" stroke-width=".6" fill="none"/>
  </svg>
  <div class="flap"><span class="seal"></span></div>
</div>
<div class="label" style="left:713px;top:307px">Envelope Back</div>

<div class="piece folder">
  <svg class="outer" viewBox="0 0 324 260" aria-hidden="true">
    <path d="M0 1 L162 1 L162 189 L299 189 L299 1 L323 2 L323 115 Q316 119 323 124 L323 188 L300 198 L300 255 L175 258 L160 200 L150 258 L22 258 L22 198 L0 188 L0 126 Q7 119 0 112Z" fill="var(--panel)"/>
  </svg>
  <div class="faint-mark" role="img" aria-label="Faint decorative background mark"></div>
  <div class="back-info">
    871 Talvenor Trade Ct<br>Marrowvale, Fl 32719<br>FL License #DL6042<br>
    <span class="icon"></span>888-555-0140<br>
    <span class="icon"></span>407-555-0146<br>
    <span class="icon"></span>407-555-0188<br>
    <span class="icon"></span>lumoraporcelain@mailvex.net<br>
    <span class="icon"></span>lumoraporcelain.net
  </div>
  <div class="cover">
    <div class="edge"></div>
    <div class="brand"><span class="brand-dot"></span><span class="brand-name"><span>Lumora</span><span>Porcelain, Inc.</span></span></div>
    <div class="tagline">Precision crafted for every smile</div>
  </div>
  <div class="pocket-card">
    <div class="brand"><span class="brand-dot"></span><span class="brand-name"><span>Lumora</span><span>Porcelain</span></span></div>
    <div class="mini">Dov Pemberly, CDT<br>Technical<br>Lisette Pemberly<br>Marketing/Office</div>
  </div>
</div>
<div class="label" style="left:1020px;top:307px">Folder</div>

</body>
</html>
```